Business Cards for Branding (Advertising) Agency

We need stylish and cool business cards.
Additional info:
1) Logo - see the attachment. You can use either the three penguins or just one penguin face (square or round) - at your discretion.
2) Text and other stuff for business card:
front side:
-Logo and company name: company name - Coastal Herons - should be in English as is in logo. This is the only exception. The rest of the text will be in Russian.
-Who we are: Брендинговое агентство
-First and last name:
-Position: Управляющий партнёр
-Address:
-Phone:
-Email:
-Website:
Note: please don't use names of information fields, such as: who we are, first and last name, position, address, phone, email and website.

3) Our suggestions on design:
-The backside of the business card can be either blank or has something on it - at your discretion.
-The business card background should be either white or grey (you can use any tone of grey).

Additional Information:
1) БРЕНДИНГОВОЕ АГЕНТСТВО
2) ул. Вересковая - these two words should be together on the same line
3) тел.: +7 (495) 381-62-09
моб.: +7 (916) 740-28-51

Reason: We would like to receive more stylish designs.

```html
<!DOCTYPE html>
<html lang="ru">
<head>
<meta charset="utf-8">
<title>Coastal Herons — визитка</title>
<link rel="stylesheet" href="https://fonts.googleapis.com/css2?family=Open+Sans:wght@300;400;600;700&display=swap">
<style>
  :root {
    --page: #e9e7e4;
    --card: #ffffff;
    --ink: #1a1a1a;
    --grey-dark: #6f6f6f;
    --grey: #8c8c8c;
    --grey-light: #b5b5b5;
    --band: #141414;
    --band-text: #ffffff;
    --accent: #f2a81d;
    --shadow: rgba(0,0,0,0.18);
  }
  * { box-sizing: border-box; margin: 0; padding: 0; }
  html, body { width: 1200px; height: 800px; overflow: hidden; }
  body {
    background: var(--page);
    font-family: "Open Sans", Arial, sans-serif;
    display: flex; align-items: center; justify-content: center; gap: 80px;
  }
  .card {
    background: var(--card);
    box-shadow: 0 10px 30px var(--shadow);
    position: relative;
    overflow: hidden;
  }
  /* back side */
  .card--back { width: 340px; height: 612px; }
  .back-logo {
    position: absolute; left: 50%; top: 50%;
    transform: translate(-50%, -50%) rotate(90deg);
    display: flex; align-items: center; gap: 16px;
    white-space: nowrap;
  }
  .back-logo__dot { width: 22px; height: 22px; border-radius: 50%; background: var(--ink); }
  .back-logo__name {
    font-weight: 300; font-size: 34px; letter-spacing: 6px;
    color: var(--ink); text-transform: uppercase;
  }
  /* front side */
  .card--front { width: 612px; height: 340px; }
  .front-brand { position: absolute; left: 40px; top: 34px; }
  .front-brand__name {
    font-weight: 300; font-size: 30px; letter-spacing: 4px;
    color: var(--grey-dark); text-transform: uppercase; line-height: 1;
  }
  .front-brand__tagline {
    margin-top: 8px; font-weight: 400; font-size: 15px; letter-spacing: 1px;
    color: var(--grey); text-transform: uppercase;
  }
  .person { position: absolute; left: 40px; top: 128px; }
  .person__name {
    font-weight: 600; font-size: 15px; letter-spacing: 0.5px;
    color: var(--grey-light); text-transform: uppercase;
  }
  .person__role { margin-top: 2px; font-size: 11px; color: var(--grey); }
  .contacts { list-style: none; margin-top: 12px; }
  .contacts li {
    display: flex; align-items: center; gap: 8px;
    font-size: 11.5px; color: var(--grey-dark); line-height: 20px;
  }
  .contacts svg { width: 12px; height: 12px; flex: none; }
  .band {
    position: absolute; left: 0; bottom: 0; width: 100%; height: 38px;
    background: var(--band);
    display: flex; align-items: center; padding-left: 22px;
  }
  .band__address {
    color: var(--band-text); font-weight: 700; font-size: 12px;
    text-transform: uppercase; letter-spacing: 0.3px;
  }
  .mascot { position: absolute; right: 0; bottom: 0; width: 260px; height: 230px; }
</style>
</head>
<body>
  <section class="card card--back" aria-label="Оборотная сторона">
    <div class="back-logo">
      <span class="back-logo__dot"></span>
      <span class="back-logo__name">Coastal Herons</span>
    </div>
  </section>

  <section class="card card--front" aria-label="Лицевая сторона">
    <header class="front-brand">
      <div class="front-brand__name">Coastal Herons</div>
      <div class="front-brand__tagline">Брендинговое агентство</div>
    </header>

    <div class="person">
      <div class="person__name">Мария Ольховская</div>
      <div class="person__role">Управляющий партнёр</div>
      <ul class="contacts">
        <li>
          <svg viewBox="0 0 12 12"><rect width="12" height="12" rx="2" fill="#9a9a9a"/><path d="M3.5 2.8l1.3 1.5-.6.9c.5 1 1.2 1.7 2.2 2.2l.9-.6 1.5 1.3-.8 1.1C5.6 9 3 6.4 2.8 3.6z" fill="#fff"/></svg>
          +7 (916) 740-28-51
        </li>
        <li>
          <svg viewBox="0 0 12 12"><rect width="12" height="12" rx="2" fill="#9a9a9a"/><path d="M2.5 3.5h7v5h-7z M2.5 3.5L6 6.5l3.5-3" fill="none" stroke="#fff" stroke-width="0.9"/></svg>
          maria@coastalherons.ru
        </li>
        <li>
          <svg viewBox="0 0 12 12"><rect width="12" height="12" rx="2" fill="#9a9a9a"/><circle cx="6" cy="6" r="3.4" fill="none" stroke="#fff" stroke-width="0.9"/><path d="M2.6 6h6.8M6 2.6c-1.6 2-1.6 4.8 0 6.8M6 2.6c1.6 2 1.6 4.8 0 6.8" fill="none" stroke="#fff" stroke-width="0.7"/></svg>
          www.coastalherons.ru
        </li>
      </ul>
    </div>

    <div class="band">
      <span class="band__address">117208, г. Москва, ул. Вересковая, д.12, стр.2</span>
    </div>

    <svg class="mascot" viewBox="0 0 260 230" role="img" aria-label="Иллюстрация: талисман агентства в шапке-ушанке">
      <defs>
        <linearGradient id="mascotTone" x1="0" y1="0" x2="1" y2="1">
          <stop offset="0" stop-color="#8a8a8a"/>
          <stop offset="0.45" stop-color="#1c1c1c"/>
          <stop offset="1" stop-color="#d9d9d9"/>
        </linearGradient>
      </defs>
      <path d="M40 230 C40 120 80 20 170 20 L260 20 L260 230 Z" fill="url(#mascotTone)"/>
    </svg>
  </section>
</body>
</html>
```